WordPress design (BRTK)

We need a wordpress design for an established auction and real estate company based in Viginia- "Don't Pause.... Propel!". The winning design will incorporate a professional color scheme with company logo in a clean layout.
Industry/Entity Type
Real Estate
Requirements
Must have
- Navigation:
- 1) Home
- 2) Services
- 3) Auctions
- 4) Gala Benefit
- 5) Appraisals
- 6) Past Successes
- 7) About BRTK
- 8) Contact us
- Colors will be those in the attached logo. design should be able to be developed in responsive theme. Wants a "very clean and professional and sharp" design. Site will have slideshow that is relatively small, not a large portion of the design. Please use stock real estate image.
- Footer will have attached logos and contact info for the client.
Nice to have
- A representative drop down menu will be nice to see.

```html
<!DOCTYPE html>
<html lang="en">
<head>
<meta charset="utf-8">
<title>BRTK Realty Group</title>
<link rel="stylesheet" href="https://fonts.googleapis.com/css2?family=Open+Sans:ital,wght@0,400;0,600;0,700;1,600&family=Cinzel:wght@400&family=Noto+Serif:wght@400&display=swap">
<style>
:root{
  --navy:#283648;
  --blue:#3e93d6;
  --cyan:#0fa8d8;
  --red:#b0101c;
  --maroon:#8c0f22;
  --ink:#2b2b2b;
  --grey:#f2f2f2;
  --side:#f4f4f4;
  --text:#444;
  --muted:#9a9a9a;
  --bar:#2a2323;
}
*{box-sizing:border-box;margin:0;padding:0}
html,body{width:1200px;height:1000px;overflow:hidden}
body{position:relative;background:#fff;font-family:"Open Sans",Arial,sans-serif;color:var(--text)}
.abs{position:absolute}
.top-right{left:1112px;top:0;width:88px;height:125px;background:var(--navy)}
.logo-box{left:88px;top:0;width:332px;height:93px}
.brand{position:absolute;left:64px;top:30px;color:#fff;font:700 30px "Open Sans",sans-serif;letter-spacing:4px}
.brand-sub{position:absolute;left:62px;top:70px;color:#fff;font:400 8px "Open Sans",sans-serif;letter-spacing:.5px}
.call{left:820px;top:16px;display:flex;align-items:center;gap:12px;color:var(--red);font-size:18px;letter-spacing:.5px}
.call-ico{width:26px;height:26px;background:var(--red);border-radius:4px;display:flex;align-items:center;justify-content:center}
.search{left:445px;top:52px;width:334px;height:29px;display:flex}
.search-field{flex:1;background:#f3f3f3;color:#aaa;font-size:13px;padding:6px 17px}
.search-btn{width:73px;background:var(--blue);color:#fff;font-size:13px;font-weight:600;text-align:center;line-height:29px}
.util{left:810px;top:54px;display:flex;align-items:center;gap:10px;color:#a5a5a5;font-size:18px}
.util span{margin-right:14px}
.social-top{display:inline-block;width:20px;height:20px;background:#b5b5b5;border-radius:3px;margin-left:16px}
.nav{left:0;top:93px;width:1200px;height:32px}
.nav ul{position:absolute;left:0;top:0;width:1200px;height:32px;list-style:none}
.nav li{position:absolute;top:0;height:32px;line-height:32px;color:#fff;font-size:14px;letter-spacing:.5px;transform:translateX(-50%);white-space:nowrap}
.nav .sep{position:absolute;top:6px;width:1px;height:20px;background:rgba(255,255,255,.25)}
.nav .active::after{content:"";position:absolute;left:-14px;right:-14px;bottom:4px;height:2px;background:var(--navy)}
.slider{left:88px;top:127px;width:722px;height:205px;background:linear-gradient(180deg,#8fb3d8 0%,#c9b49a 55%,#9c7a56 100%)}
.slider-bar{left:88px;top:332px;width:722px;height:30px;background:var(--navy)}
.dots{position:absolute;left:188px;top:8px;display:flex;align-items:center;gap:8px}
.arrow-btn{width:18px;height:18px;border-radius:50%;background:#fff;color:var(--navy);font-size:12px;font-weight:700;display:flex;align-items:center;justify-content:center}
.dot{width:28px;height:3px;background:#fff}
.dot.on{background:var(--cyan)}
.dots .arrow-btn:first-child{margin-right:12px}
.dots .arrow-btn:last-child{margin-left:12px}
.auction{left:662px;top:240px;width:148px;height:122px}
.listings{left:88px;top:368px;width:720px;height:322px;background:var(--grey)}
.card{position:absolute;top:22px;width:196px;text-align:center}
.card-photo{width:194px;height:106px;margin:0 auto;background:linear-gradient(180deg,#6aa6dd 0%,#b9d1e6 45%,#cfa77d 62%,#8a9a62 100%);border:2px solid #fff;box-shadow:0 1px 4px rgba(0,0,0,.2)}
.price{position:relative;margin:-14px auto 0;width:130px;height:36px;background:var(--cyan);border:3px solid #fff;border-radius:6px;color:#fff;font-size:16px;font-weight:600;line-height:30px;box-shadow:0 1px 3px rgba(0,0,0,.2)}
.status{margin-top:10px;font-size:12.5px;color:#333}
.facts{margin:16px auto 0;width:196px;height:50px;background:#fff;font:400 9px "Noto Serif",serif;color:#888;text-align:left;padding:5px 10px;line-height:25px}
.facts i{display:inline-block;width:8px;height:7px;background:#999;margin-right:4px;vertical-align:-1px;font-style:normal}
.facts span{margin-right:10px}
.view{margin:19px auto 0;width:124px;height:32px;border:2px solid #ddd;border-radius:6px;background:#fff;font-size:10.5px;font-weight:600;color:#333;line-height:28px;letter-spacing:.3px}
.col-sep{position:absolute;top:30px;width:1px;height:268px;background:#dcdcdc}
.pager{left:585px;top:691px;width:223px;height:32px;color:#fff}
.pager-txt{position:absolute;left:25px;top:6px;font:italic 600 13px "Open Sans",sans-serif}
.pg{position:absolute;top:7px;width:17px;height:17px;font-size:10px;text-align:center;line-height:17px;background:#fff;color:#333;border-radius:2px}
.pg.cur{background:var(--navy);color:#fff}
.badges{left:88px;top:740px;width:720px;height:70px}
.badge{position:absolute;top:0;background:#c9ced6;border-radius:4px}
.sidebar{left:824px;top:125px;width:288px;height:701px;background:var(--side)}
.side-h{position:absolute;left:22px;width:244px;text-align:center;font:400 15px "Cinzel",serif;color:#555;letter-spacing:1px;padding-bottom:6px;border-bottom:2px solid #e6e6e6}
.field{position:absolute;left:22px;height:25px;background:#fff;font:italic 400 11px "Noto Serif",serif;color:#999;padding:5px 10px}
.drop{position:absolute;width:24px;height:25px;background:var(--maroon)}
.go{position:absolute;left:214px;width:33px;height:25px;background:var(--blue);color:#fff;font-size:13px;font-weight:600;text-align:center;line-height:25px}
.recent{position:absolute;left:22px;top:295px;list-style:none;font:400 13px "Noto Serif",serif;color:#777}
.recent li{height:24px;padding-left:21px;position:relative}
.recent li::before{content:"";position:absolute;left:0;top:5px;border:4px solid transparent;border-left:7px solid #999}
.more{position:absolute;left:43px;top:470px;font:400 11px "Cinzel",serif;color:var(--blue);letter-spacing:.5px}
.auth{position:absolute;left:22px;top:510px;width:244px;font:400 15px "Cinzel",serif;color:#555;letter-spacing:1px;border-bottom:2px solid #e6e6e6;padding-bottom:6px}
.auth span{display:inline-block}
.input{position:absolute;left:22px;width:226px;height:23px;background:#fff;font-size:11px;color:#777;padding:4px 10px}
.forgot{position:absolute;left:171px;top:631px;font-size:9px;color:#234b8f;text-decoration:underline}
.submit-side{position:absolute;left:160px;top:653px;width:89px;height:24px;background:var(--maroon);border-radius:4px;color:#fff;font-size:11px;font-weight:700;text-align:center;line-height:24px}
.footer{left:0;top:845px;width:1200px;height:133px;background:var(--navy)}
.foot-h{position:absolute;top:13px;color:#fff;font-size:16px;font-weight:600;letter-spacing:.3px}
.f-input{position:absolute;left:87px;width:198px;height:22px;background:#000;color:#bbb;font-size:11.5px;padding:3px 12px}
.f-submit{position:absolute;left:208px;top:100px;width:77px;height:22px;background:#c8141c;color:#fff;font-size:13px;font-weight:600;text-align:center;line-height:22px}
.quote{position:absolute;left:368px;top:38px;width:222px;font-size:11px;line-height:15px;color:#fff}
.by{position:absolute;left:547px;top:96px;font-size:11px;color:#6fb3ea}
.soc{position:absolute;width:20px;height:20px;border-radius:50%;background:#fff;opacity:.9}
.contacts{position:absolute;right:88px;top:38px;text-align:right;color:#fff;font-size:13px;line-height:16.6px}
.copy{left:0;top:978px;width:1200px;height:22px;background:var(--bar);color:#c9c9c9;font-size:11px;text-align:center;line-height:24px}
</style>
</head>
<body>
<div class="abs top-right"></div>

<header>
  <div class="abs logo-box">
    <svg width="332" height="93" viewBox="0 0 332 93"><polygon points="0,17 332,17 300,93 0,93" fill="#2b2b2b"/><rect x="40" y="38" width="14" height="14" fill="#c4a24a"/></svg>
    <div class="brand" style="left:66px">BRTK</div>
    <div class="brand-sub">BRTK REALTY GROUP, INC. · AUCTION · APPRAISALS</div>
  </div>
  <div class="abs call">
    <div class="call-ico"><svg width="14" height="14" viewBox="0 0 24 24"><path d="M6.6 10.8a15 15 0 0 0 6.6 6.6l2.2-2.2c.3-.3.7-.4 1-.2 1.1.4 2.3.6 3.6.6.6 0 1 .4 1 1V20c0 .6-.4 1-1 1A17 17 0 0 1 3 4c0-.6.4-1 1-1h3.5c.6 0 1 .4 1 1 0 1.3.2 2.5.6 3.6.1.3 0 .7-.2 1z" fill="#fff"/></svg></div>
    <span>CALL ON : (540) 555-0172</span>
  </div>
  <div class="abs search"><div class="search-field">Type Here . . .</div><div class="search-btn">SEARCH</div></div>
  <div class="abs util">
    <svg width="12" height="13" viewBox="0 0 12 13"><circle cx="6" cy="4" r="3" fill="#aaa"/><path d="M0 13c0-4 3-5 6-5s6 1 6 5z" fill="#aaa"/></svg><span>Login</span>
    <svg width="16" height="16" viewBox="0 0 16 16"><circle cx="8" cy="8" r="6" fill="none" stroke="#aaa" stroke-width="2.5"/></svg><span>help</span>
    <i class="social-top"></i><i class="social-top" style="border-radius:50%"></i><i class="social-top"></i>
  </div>
  <nav class="abs nav">
    <svg class="abs" width="1200" height="32" viewBox="0 0 1200 32"><rect width="1200" height="32" fill="#283648"/><polygon points="0,0 392,0 420,32 0,32" fill="#3e93d6"/></svg>
    <ul>
      <li class="active" style="left:186px">HOME</li>
      <li style="left:315px">ABOUT US</li>
      <li style="left:472px">PROPERTIES <svg width="9" height="8" viewBox="0 0 9 8"><polygon points="0,0 9,0 4.5,7" fill="#fff"/></svg></li>
      <li style="left:610px">AGENTS</li>
      <li style="left:735px">NEWS</li>
      <li style="left:850px">CONTACT</li>
      <li style="left:973px">DISCLAIMER</li>
    </ul>
    <i class="sep" style="left:246px"></i><i class="sep" style="left:534px"></i><i class="sep" style="left:667px"></i><i class="sep" style="left:787px"></i><i class="sep" style="left:907px"></i>
  </nav>
</header>

<main>
  <div class="abs slider" role="img" aria-label="Stock photo of a couple looking at a stucco two-storey house"></div>
  <div class="abs slider-bar">
    <div class="dots"><span class="arrow-btn">‹</span><i class="dot"></i><i class="dot on"></i><i class="dot"></i><i class="dot"></i><i class="dot"></i><i class="dot"></i><span class="arrow-btn">›</span></div>
  </div>
  <div class="abs auction">
    <svg width="148" height="122" viewBox="0 0 148 122"><polygon points="148,0 148,122 0,122" fill="#a80f1e"/><text x="92" y="100" fill="#fff" font-family="Open Sans, sans-serif" font-weight="700" font-size="19" transform="rotate(-40 92 100)" text-anchor="middle">AUCTION</text><text x="108" y="108" fill="#fff" font-family="Open Sans, sans-serif" font-size="10" transform="rotate(-40 108 108)" text-anchor="middle">CLICK HERE</text></svg>
  </div>

  <section class="abs listings">
    <article class="card" style="left:13px">
      <div class="card-photo" role="img" aria-label="Photo of a two-storey house with garage"></div>
      <div class="price">$65,00,000</div>
      <div class="status">Property Status&nbsp; - &nbsp;FOR SALE</div>
      <div class="facts"><span><i></i>4000 sqft</span><span><i></i>6 Beds</span><span><i></i>4.5 Baths</span><br><span><i></i>2 Car Garage</span><span><i></i>Listed 1 year ago</span></div>
      <div class="view">VIEW THE LISTING</div>
    </article>
    <i class="col-sep" style="left:236px"></i>
    <article class="card" style="left:265px">
      <div class="card-photo" role="img" aria-label="Photo of a two-storey house with garage"></div>
      <div class="price">$65,00,000</div>
      <div class="status">Property Status&nbsp; - &nbsp;FOR RENT</div>
      <div class="facts"><span><i></i>4000 sqft</span><span><i></i>6 Beds</span><span><i></i>4.5 Baths</span><br><span><i></i>2 Car Garage</span><span><i></i>Listed 1 year ago</span></div>
      <div class="view">VIEW THE LISTING</div>
    </article>
    <i class="col-sep" style="left:487px"></i>
    <article class="card" style="left:509px">
      <div class="card-photo" role="img" aria-label="Photo of a two-storey house with garage"></div>
      <div class="price">$65,00,000</div>
      <div class="status">Property Status&nbsp; - &nbsp;OPEN HOUSE</div>
      <div class="facts"><span><i></i>4000 sqft</span><span><i></i>6 Beds</span><span><i></i>4.5 Baths</span><br><span><i></i>2 Car Garage</span><span><i></i>Listed 1 year ago</span></div>
      <div class="view">VIEW THE LISTING</div>
    </article>
  </section>

  <div class="abs pager">
    <svg class="abs" width="223" height="32" viewBox="0 0 223 32"><polygon points="0,0 223,0 223,32 16,32" fill="#0fa8d8"/></svg>
    <span class="pager-txt">Page 1 of 3</span>
    <span class="pg cur" style="left:104px">1</span><span class="pg" style="left:128px">2</span><span class="pg" style="left:153px">3</span>
    <span class="pager-txt" style="left:183px;top:5px">&gt;&gt;</span>
  </div>

  <div class="abs badges">
    <svg class="abs" style="left:0;top:15px" width="16" height="34" viewBox="0 0 16 34"><polyline points="14,2 3,17 14,32" fill="none" stroke="#283648" stroke-width="3"/></svg>
    <div class="badge" style="left:34px;top:8px;width:50px;height:57px"></div>
    <div class="badge" style="left:107px;top:10px;width:62px;height:54px;border-radius:50%"></div>
    <div class="badge" style="left:192px;top:6px;width:118px;height:56px"></div>
    <div class="badge" style="left:328px;top:2px;width:66px;height:66px;border-radius:50%"></div>
    <div class="badge" style="left:425px;top:2px;width:129px;height:63px;background:#3a3a3a"></div>
    <div class="badge" style="left:580px;top:2px;width:104px;height:62px"></div>
    <svg class="abs" style="left:700px;top:15px" width="16" height="34" viewBox="0 0 16 34"><polyline points="2,2 13,17 2,32" fill="none" stroke="#283648" stroke-width="3"/></svg>
  </div>

  <aside class="abs sidebar">
    <div class="side-h" style="top:8px">Property Search</div>
    <div class="field" style="top:48px;width:190px">Find Properties</div><div class="go" style="top:48px">GO</div>
    <div class="field" style="top:97px;width:162px">Select By Price</div><div class="drop" style="left:184px;top:97px"><svg width="24" height="25" viewBox="0 0 24 25"><polygon points="6,9 18,9 12,17" fill="#fff"/></svg></div><div class="go" style="top:97px">GO</div>
    <div class="field" style="top:145px;width:162px">Select By Location</div><div class="drop" style="left:184px;top:145px"><svg width="24" height="25" viewBox="0 0 24 25"><polygon points="6,9 18,9 12,17" fill="#fff"/></svg></div><div class="go" style="top:145px">GO</div>
    <div class="field" style="top:192px;width:162px">Select By Type</div><div class="drop" style="left:184px;top:192px"><svg width="24" height="25" viewBox="0 0 24 25"><polygon points="6,9 18,9 12,17" fill="#fff"/></svg></div><div class="go" style="top:192px">GO</div>
    <div class="side-h" style="top:253px">Recent Listing</div>
    <ul class="recent">
      <li>House On The Beach</li><li>Desert Aesthetic</li><li>Classic Brick Building</li><li>Limestone Estate</li><li>Las Angles Mansion</li><li>To House a Family</li><li>The Urban Life</li>
    </ul>
    <div class="more">More &gt;&gt;</div>
    <div class="auth"><span style="margin-left:19px">Login</span><span style="margin-left:46px;color:#999">|</span><span style="margin-left:22px">Sign Up</span></div>
    <div class="input" style="top:563px">Username</div>
    <div class="input" style="top:603px">Password</div>
    <div class="forgot">Forgot Password</div>
    <div class="submit-side">SUBMIT</div>
  </aside>
</main>

<footer class="abs footer">
  <svg class="abs" width="1200" height="133" viewBox="0 0 1200 133"><polygon points="633,0 1200,0 1200,133 676,133" fill="#3e93d6"/><line x1="316" y1="12" x2="316" y2="120" stroke="#3a4a5e"/><line x1="813" y1="12" x2="813" y2="133" stroke="#2f7cbd"/></svg>
  <div class="foot-h" style="left:87px">SUBSCRIBE NEWS LETTER</div>
  <div class="f-input" style="top:41px">First name</div>
  <div class="f-input" style="top:71px">Email Id</div>
  <div class="f-submit">Submit</div>
  <div class="foot-h" style="left:412px">TESTIMONIALS</div>
  <p class="quote">"Lorem ipsum dolor sit amet, consectetur elit. Pellentesque ut loborts tortor. Duis ut accumsan neque. Morbi iaculis neque eget venenatis"</p>
  <span class="by">By ABC</span>
  <div class="foot-h" style="left:726px">GET IN TOUCH</div>
  <i class="soc" style="left:728px;top:45px"></i><i class="soc" style="left:757px;top:45px"></i><i class="soc" style="left:785px;top:45px"></i><i class="soc" style="left:814px;top:45px"></i>
  <i class="soc" style="left:728px;top:73px"></i><i class="soc" style="left:757px;top:73px"></i><i class="soc" style="left:785px;top:73px"></i>
  <div class="foot-h" style="left:995px">CONTACTS</div>
  <div class="contacts">Location : 48 Harbor Crest Road,<br>Fairlane, Viginia 22150-4417<br>Phone :&nbsp; (800) 555-01234<br>Mobile :&nbsp; (800) 555-01234<br>Email : info@brtk.com</div>
</footer>
<div class="abs copy">© &nbsp;2013-2014 BRTK. All Rights Reserved.</div>
</body>
</html>
```